Thai Restruant Business Card Design

A Business card design for a Thai and Laos take away restaurant.

We are a highly respectable take away restaurant in a small shopping center.

The design must have a Papaya Tree and Thai Palace.

The final design should communicate, innovation, fun and delicious food.

Industry/Entity Type

Restaurant

Contact Information for Business Card

Mango Hearth, Thai & Lao Food, Shop 4. 71 Elm Lane. Fairholme N.S.W 2174, Tel. 02-96415270, Open 7 Days From 9.00am To 7.00pm

```html
<!DOCTYPE html>
<html lang="en">
<head>
<meta charset="utf-8">
<title>Mango Hearth – Business Card</title>
<link rel="stylesheet" href="https://fonts.googleapis.com/css2?family=Open+Sans:wght@400;500&display=swap">
<style>
  :root {
    --stage: #857a6f;
    --card: #ffffff;
    --brand-green: #3f7a35;
    --ink: #1d1d1b;
    --palace-light: #f1efea;
    --palace-mid: #d9d4c8;
    --palace-warm: #cdbb95;
    --sky: #bcd9ea;
    --leaf: #3f7d3a;
    --leaf-dark: #2a5a2a;
    --fruit: #e89a2c;
  }
  html, body {
    margin: 0;
    width: 1200px;
    height: 707px;
    overflow: hidden;
    background: var(--stage);
  }
  .business-card {
    position: absolute;
    left: 100px;
    top: 76px;
    width: 1000px;
    height: 556px;
    box-shadow: 0 12px 30px rgba(0,0,0,0.25);
    background: var(--card);
  }
  .business-card svg { display: block; }
  .brand-name, .brand-tagline { fill: var(--brand-green); }
  .contact-line, .hours-line { fill: var(--ink); }
  .card-text { font-family: "Open Sans", sans-serif; text-anchor: middle; }
</style>
</head>
<body>
  <div class="business-card">
    <svg width="1000" height="556" viewBox="0 0 1000 556" xmlns="http://www.w3.org/2000/svg">
      <defs>
        <linearGradient id="palaceTones" x1="0" y1="0" x2="1" y2="1">
          <stop offset="0" stop-color="var(--palace-light)"/>
          <stop offset="0.5" stop-color="var(--palace-mid)"/>
          <stop offset="0.8" stop-color="var(--palace-warm)" stop-opacity="0.7"/>
          <stop offset="1" stop-color="var(--palace-light)"/>
        </linearGradient>
        <linearGradient id="papayaTones" x1="0" y1="0" x2="1" y2="1">
          <stop offset="0" stop-color="var(--sky)"/>
          <stop offset="0.35" stop-color="var(--leaf)"/>
          <stop offset="0.65" stop-color="var(--fruit)"/>
          <stop offset="1" stop-color="var(--leaf-dark)"/>
        </linearGradient>
      </defs>

      <rect class="palace-backdrop" x="0" y="0" width="1000" height="556" fill="url(#palaceTones)" role="img" aria-label="Faded photograph of a Thai palace with ornate golden roofs and trees"/>
      <rect class="palace-veil" x="0" y="0" width="1000" height="556" fill="#ffffff" opacity="0.35"/>

      <polygon class="divider-stripe" points="905,0 1000,0 1000,556 525,556" fill="var(--card)"/>
      <polygon class="papaya-tree" points="940,0 1000,0 1000,556 565,556" fill="url(#papayaTones)" role="img" aria-label="Illustration of a papaya tree with green leaves and ripe orange papayas against a blue sky"/>

      <g class="card-text">
        <text class="brand-name" x="367" y="104" font-size="62" font-weight="400" letter-spacing="2">Mango Hearth</text>
        <text class="brand-tagline" x="350" y="184" font-size="37" letter-spacing="1">Thai &amp; Lao Food</text>
        <text class="contact-line" x="340" y="274" font-size="34" letter-spacing="1">Shop 4. 71 Elm Lane.</text>
        <text class="contact-line" x="340" y="322" font-size="34" letter-spacing="1">Fairholme N.S.W 2174</text>
        <text class="contact-line" x="340" y="382" font-size="40" letter-spacing="1">Tel. 02-96415270</text>
        <text class="hours-line" x="320" y="449" font-size="27">Open 7 Days</text>
        <text class="hours-line" x="320" y="496" font-size="27">From 9.00am To 7.00pm</text>
      </g>
    </svg>
  </div>
</body>
</html>
```